Business Card Design Project

Hello! We need a business card design for a new company opening up in Downtown Dallas called Marbury Cupcakes. We are a cupcake factory and our primary colors are Tiffany Blue and Brown. We want to have a design that can be used for multiple positions (Owner/Operations Manager, Assistant Operations Manager, Decorator, Baker, Corporate Sale Rep, Special Events Rep etc) We would like for it to be double sided. Use the following information in your designs:

Renata Vankirk
Assistant Operations Manager
renata@marburycupcakes.example
T555.318.4907

Store Hours:
Mon-Thur 10am-9pm
Fri-Sat 10am-10pm
Sun 12pm-7pm

website: www.marburycupcakes.example

Address: 2735 Birch Ave, Dallas TX 70519

The logo is attached.

Industry/Entity Type

Business

Requirements
Must have
• It must be Tiffany Blue and Brown.
Nice to have
• Nice for it to be double sided.
Should not have
• No graphics like a cupcake. Just the word logo.

```html
<!DOCTYPE html>
<html lang="en">
<head>
<meta charset="utf-8">
<title>Marbury Cupcakes – Business Card</title>
<link rel="stylesheet" href="https://fonts.googleapis.com/css2?family=Questrial&display=swap">
<style>
  :root {
    --tiffany: #72bec6;
    --brown: #4a2a22;
    --white: #ffffff;
    --rule: #e4e4e4;
    --backdrop: #3a3a3a;
  }
  * { box-sizing: border-box; margin: 0; padding: 0; }
  html, body { width: 1200px; height: 900px; overflow: hidden; }
  body {
    background: var(--backdrop);
    font-family: "Questrial", "Helvetica Neue", Arial, sans-serif;
    position: relative;
  }
  .card {
    position: absolute;
    top: 290px;
    width: 530px;
    height: 325px;
    border-radius: 24px;
    overflow: hidden;
  }
  .card--front { left: 50px; background: var(--tiffany); }
  .card--back { left: 620px; background: var(--white); }
  .card__wave {
    position: absolute;
    left: 0; top: 0;
    width: 530px; height: 325px;
  }
  .wordmark {
    position: absolute;
    font-weight: 400;
    line-height: 1;
    white-space: nowrap;
  }
  .card--front .wordmark {
    left: 0; right: 0;
    top: 122px;
    text-align: center;
    font-size: 50px;
    color: var(--white);
  }
  .card--back .wordmark {
    left: 30px;
    top: 70px;
    font-size: 30px;
    color: var(--tiffany);
  }
  .website {
    position: absolute;
    left: 0; right: 0;
    top: 280px;
    text-align: center;
    font-size: 17px;
    color: var(--brown);
    letter-spacing: 0.5px;
  }
  .store-hours {
    position: absolute;
    right: 0;
    top: 49px;
    width: 186px;
    height: 80px;
    background: var(--tiffany);
    border-bottom-left-radius: 40px;
    color: var(--white);
    text-align: right;
    padding: 10px 28px 0 0;
    font-size: 13px;
    line-height: 15px;
  }
  .contact {
    position: absolute;
    left: 0; right: 0;
    top: 160px;
    text-align: center;
    color: var(--brown);
  }
  .contact__name { font-size: 25px; color: var(--tiffany); line-height: 30px; }
  .contact__title { font-size: 15px; margin-top: 4px; letter-spacing: 0.3px; }
  .contact__line { font-size: 13px; line-height: 16px; }
  .contact__title + .contact__line { margin-top: 10px; }
  .address {
    position: absolute;
    left: 0; right: 0;
    top: 282px;
    text-align: center;
    font-size: 13px;
    color: var(--white);
  }
</style>
</head>
<body>
  <section class="card card--front" aria-label="Card front">
    <svg class="card__wave" viewBox="0 0 530 325" aria-hidden="true">
      <path d="M0 275 Q265 248 530 275" fill="none" stroke="var(--rule)" stroke-width="5"/>
      <path d="M0 280 Q265 253 530 280 L530 325 L0 325 Z" fill="var(--white)"/>
    </svg>
    <p class="wordmark">Marbury Cupcakes</p>
    <p class="website">www.marburycupcakes.example</p>
  </section>

  <section class="card card--back" aria-label="Card back">
    <svg class="card__wave" viewBox="0 0 530 325" aria-hidden="true">
      <path d="M0 275 Q265 248 530 275" fill="none" stroke="var(--rule)" stroke-width="5"/>
      <path d="M0 280 Q265 253 530 280 L530 325 L0 325 Z" fill="var(--tiffany)"/>
    </svg>
    <p class="wordmark">Marbury Cupcakes</p>
    <div class="store-hours">
      <p>Store Hours:</p>
      <p>Mon-Thur 10am-9pm</p>
      <p>Fri-Sat 10am-10pm</p>
      <p>Sun 12pm-7pm</p>
    </div>
    <div class="contact">
      <p class="contact__name">Renata Vankirk</p>
      <p class="contact__title">Assistant Operations Manager</p>
      <p class="contact__line">Phone: 555.318.4907</p>
      <p class="contact__line">Mail: renata@marburycupcakes.example</p>
    </div>
    <p class="address">Address: 2735 Birch Ave, Dallas TX 70519</p>
  </section>
</body>
</html>
```